K9 Orbit needs a business card designed

We need a business card designed for K9 Orbit, an expansion of K9 Systems Pty Ltd (www.k9systems.com.au)

We provide high quality professional services for the Australian space industry. Our clients include the Southern Launch Bureau and companies working in the space industry. We identify people with space related skills both locally and internationally who are then contracted by clients to create products and support space launch activities.

Colours to be used:
- Navy blue #000080
- Rocket metallic #8A7F8D
- Platinum #E5E4E2
- Black #000000
- White #FFFFFF

*Front of the card*
I have attached our K9 Orbit logo, which needs to be the main item on the card. The 'Space' text should be placed to the right of the 'K9' part rather than below, similar to the attached K9 Systems card, which this card should match.

If subtext is included, however, it should read ‘Labour Hire • Consultancy • Project Delivery’ rather than the ‘Design • Build • Test • Maintain’ of the K9 Systems card.

A black background (rather than blue background in the K9 Systems card) might be good, with a white pattern as in the K9 Systems card. If colour is used, the logo should be in its standard colours (as provided for the K9 Orbit logo).

*Back of the card*
Include a smaller K9 Orbit logo on the back.

We need the following details for K9 Orbit personnel (as a template for entry):
- Name
- Company Position
- Mobile Number
- Email
- Office Address
- Include the K9 Orbit website: www.k9orbit.com.au

Overall, we'd like to see a design that communicates the adventure of space, professional integrity, and customer service. We look forward to seeing what you can come up with.

Target Market(s)

We provide high quality professional services for the Australian space industry. Our clients include the Southern Launch Bureau and companies working in the space industry.

Contact Information for Business Card

- Name
- Company Position
- Mobile Number
- Email
- Office Address

Requirements
Must have
• See project description.

```html
<!DOCTYPE html>
<html lang="en">
<head>
<meta charset="utf-8">
<title>K9 Orbit Business Card</title>
<link href="https://fonts.googleapis.com/css2?family=Arimo:wght@400;700&display=swap" rel="stylesheet">
<style>
  :root {
    --navy: #262872;
    --navy-deep: #25276f;
    --metal: #8a7f8d;
    --ink: #2b2b2b;
    --white: #ffffff;
    --stage: #a3a3a3;
    --mark-light: #6f73e6;
  }
  * { margin: 0; padding: 0; box-sizing: border-box; }
  html, body {
    width: 1200px; height: 1200px; overflow: hidden;
    background: var(--stage);
  }
  .card {
    position: absolute; left: 160px; width: 880px; height: 503px;
    font-family: "Arimo", sans-serif;
  }
  .card-front { top: 70px; background: var(--white); }
  .card-back { top: 630px; background: var(--navy-deep); }

  .brand { position: absolute; display: flex; align-items: center; }
  .brand-dot { border-radius: 50%; flex: none; }
  .brand-name { font-weight: 400; white-space: nowrap; line-height: 1; }

  .card-front .brand { left: 150px; top: 226px; }
  .card-front .brand-dot { width: 36px; height: 36px; background: var(--navy); margin-right: 16px; }
  .card-front .brand-name { font-size: 52px; color: var(--navy); }

  .divider {
    position: absolute; left: 501px; top: 135px; width: 1.5px; height: 206px;
    background: var(--ink);
  }
  .contact { position: absolute; left: 536px; top: 133px; }
  .contact-name { font-size: 28px; font-weight: 700; color: var(--navy); line-height: 1.1; }
  .contact-role { font-size: 19px; color: var(--metal); margin-top: 4px; }
  .contact-address { font-size: 19px; color: var(--ink); line-height: 25px; margin-top: 14px; }
  .contact-lines { font-size: 19px; color: var(--ink); line-height: 25px; margin-top: 10px; margin-left: 3px; }

  .band { position: absolute; left: 0; top: 418px; width: 880px; height: 37px; display: flex; }
  .band-navy { width: 706px; background: var(--navy); position: relative; color: var(--white); }
  .band-web { position: absolute; left: 193px; top: 8px; font-size: 19px; letter-spacing: 1.6px; }
  .band-mark { position: absolute; right: 10px; top: 8px; font-size: 19px; }
  .band-metal { flex: 1; background: var(--metal); }

  .card-back .brand { left: 250px; top: 214px; }
  .card-back .brand-dot { width: 52px; height: 52px; background: var(--mark-light); margin-right: 24px; }
  .card-back .brand-name { font-size: 80px; color: var(--mark-light); }
</style>
</head>
<body>
  <section class="card card-front" aria-label="Card front">
    <div class="brand">
      <span class="brand-dot"></span>
      <span class="brand-name">K9 Orbit</span>
    </div>

    <div class="divider"></div>

    <div class="contact">
      <p class="contact-name">Daniel Archer</p>
      <p class="contact-role">President</p>
      <p class="contact-address">K9 Orbit LLC<br>4120 Wattle Grove Road<br>Ridgeview, Tasmania 7055</p>
      <p class="contact-lines">P. 0491 570 238<br>info@k9orbit.com.au</p>
    </div>

    <div class="band">
      <div class="band-navy">
        <span class="band-web">www.K9ORBIT.com.au</span>
        <span class="band-mark">K9 Orbit</span>
      </div>
      <div class="band-metal"></div>
    </div>
  </section>

  <section class="card card-back" aria-label="Card back">
    <div class="brand">
      <span class="brand-dot"></span>
      <span class="brand-name">K9 Orbit</span>
    </div>
  </section>
</body>
</html>
```